Pause Your Day And Browse- PYDAB poster

I am the Vice President of Advocacy for the Coastal School Bookkeepers Guild. I am looking to have a set of posters made for PYDAB (Pause Your Day and Browse) October 23. PYDAB is a time when all school children in BC are encouraged to Pause Your Day and Browse for 15-20 minutes at some point in their day.

I would like to get a set of 2 digital posters designed (if possible it would be nice to have the option to print to both 11 x 17 and 8.5 x 11 paper). We need a poster that is high school (Grade 8-12) appropriate and one that is elementary (Grade k-7) appropriate. Both posters need to be replicated in French. All posters need to have the PEWU logo on them as well as the Coastal School Bookkeepers Guild Logo.

Here is a link to last year's successful design http://pewu-sample.ca/csbg/info/outreach.html
There are two additional samples in the uploaded files section.

Each poster needs to have the following information:

-Pause Your Day and Browse (PYDAB)
- The date Monday, October 23, 2017
-the logo for the PEWU (attached)
-the logo for the CSBG (attached)- the logos do not have to be large.

Target Market(s)

Children ages 5-12 and 12-17 as well as their teachers

Industry/Entity Type

Teacher

Font styles to use
Sans Serif

Requirements
Must have
• Must have both logos- colours may be changed for either or both
Nice to have
• Clear, Bright lettering. Images of child or children enjoying reading
Should not have
• stereotypes

```html
<!DOCTYPE html>
<html lang="en">
<head>
<meta charset="utf-8">
<title>Pause Your Day And Browse- PYDAB poster</title>
<link rel="stylesheet" href="https://fonts.googleapis.com/css2?family=Josefin+Sans:wght@600&family=Marcellus&display=swap">
<style>
  :root {
    --page: #ffffff;
    --bark-dark: #3b2a20;
    --bark: #6a4a36;
    --leaf-dark: #2f4a26;
    --leaf: #6f8a3c;
    --sun: #d8c98a;
    --ink-light: #ffffff;
    --ink-dark: #1a1a1a;
    --divider: #d98a6a;
    --guild-green: #2e6b2f;
    --union-blue: #1f4f9a;
  }
  * { margin: 0; padding: 0; box-sizing: border-box; }
  html, body {
    width: 1200px; height: 776px; overflow: hidden;
    background: var(--page);
  }
  .poster {
    position: absolute; left: 62px; top: 42px;
    width: 1078px; height: 696px; overflow: hidden;
    box-shadow: 4px 5px 8px rgba(0,0,0,0.45);
  }
  .backdrop {
    position: absolute; inset: 0;
    background:
      radial-gradient(ellipse 420px 300px at 160px 300px, rgba(111,138,60,0.85), transparent 70%),
      radial-gradient(ellipse 300px 260px at 60px 560px, rgba(216,201,138,0.7), transparent 70%),
      linear-gradient(100deg, var(--leaf-dark) 0%, var(--leaf) 22%, var(--bark) 45%, var(--bark-dark) 62%, var(--bark) 80%, var(--bark-dark) 100%);
  }
  .title {
    position: absolute; left: 0; right: 0; top: 118px;
    text-align: center;
    font-family: "Josefin Sans", sans-serif; font-weight: 600;
    font-size: 300px; line-height: 1; letter-spacing: 6px;
    color: var(--ink-light);
  }
  .subtitle {
    position: absolute; left: 0; right: 0; top: 470px;
    text-align: center;
    font-family: "Marcellus", serif;
    font-size: 47px; letter-spacing: 1px;
    color: var(--ink-light);
  }
  .date-band {
    position: absolute; left: 0; right: 0; top: 563px; bottom: 0;
    background: linear-gradient(90deg, rgba(255,255,255,0.55) 0%, rgba(255,255,255,0.8) 45%, #ffffff 75%);
  }
  .date {
    position: absolute; left: 0; top: 44px; height: 56px;
    display: flex; align-items: center;
    font-family: "Marcellus", serif; font-size: 46px;
    color: var(--ink-dark);
  }
  .date span { padding: 0 14px; }
  .date span:first-child { padding-left: 138px; }
  .date .rule { width: 5px; height: 74px; background: var(--divider); padding: 0; }
  .partners {
    position: absolute; right: 26px; top: 20px;
    display: flex; align-items: center; gap: 34px;
    font-family: "Marcellus", serif;
  }
  .partner { display: flex; align-items: center; gap: 10px; font-size: 30px; }
  .partner--guild { color: var(--guild-green); }
  .partner--union { color: var(--union-blue); }
  .partner .mark-square { width: 22px; height: 22px; background: var(--guild-green); }
  .partner .mark-circle { width: 26px; height: 26px; border-radius: 50%; background: var(--union-blue); }
</style>
</head>
<body>
  <main class="poster">
    <div class="backdrop" role="img" aria-label="Photograph of a large tree trunk and branch in a sunlit green park"></div>
    <h1 class="title">PYDAB</h1>
    <p class="subtitle">PAUSE YOUR DAY AND BROWSE</p>
    <footer class="date-band">
      <p class="date">
        <span>Monday</span><span class="rule"></span><span>October 23</span><span class="rule"></span><span>2017</span>
      </p>
      <div class="partners">
        <div class="partner partner--guild"><span class="mark-square"></span>CSBG</div>
        <div class="partner partner--union"><span class="mark-circle"></span>PEWU</div>
      </div>
    </footer>
  </main>
</body>
</html>
```